Medical group practice

We need a flyer design incorporating the three doctors in the practice, there is a general practitioner, ophthalmologist and an obstetrician & Gynaecologist. see the attached file for the concept. will leave the colour design up to you

Target Market(s)

general public

Industry/Entity Type

Health Care

Colors

Designer to choose colors to be used in the design.

Requirements
Must have
• logos included in attachement

```html
<!DOCTYPE html>
<html lang="en">
<head>
<meta charset="utf-8">
<title>Keystone Medical – Flyer</title>
<link rel="stylesheet" href="https://fonts.googleapis.com/css2?family=Fira+Sans:ital,wght@0,400;0,500;0,600;0,700;1,400;1,500;1,600&display=swap">
<style>
  :root{
    --bg:#9e9e9e;
    --paper:#ffffff;
    --red:#e21f26;
    --grey:#555a60;
    --ink:#2b2b2b;
    --teal:#00a0bf;
    --teal-dark:#007d96;
    --purple:#68246b;
    --purple-dark:#4a0f4c;
    --navy:#1f2a5e;
    --navy-dark:#0f1840;
    --white:#ffffff;
  }
  *{margin:0;padding:0;box-sizing:border-box}
  html,body{width:1200px;height:1000px;overflow:hidden}
  body{background:var(--bg);font-family:"Fira Sans",Arial,sans-serif;position:relative;color:var(--ink)}
  .flyer{position:absolute;left:316px;top:62px;width:620px;height:876px;background:var(--paper);box-shadow:0 4px 14px rgba(0,0,0,.35)}
  .top-band{position:absolute;left:0;top:0;width:100%;height:28px;background:var(--red)}

  .brand-dot{position:absolute;left:60px;top:62px;width:64px;height:64px;border-radius:50%;background:var(--red)}
  .brand-name{position:absolute;left:130px;top:60px;width:400px;text-align:center;font-weight:700;font-size:33px;letter-spacing:.5px;color:var(--red);line-height:1}
  .tagline{position:absolute;left:130px;top:98px;width:400px;display:flex;align-items:center;gap:10px;font-style:italic;font-weight:500;font-size:17px;color:#333}
  .tagline::before,.tagline::after{content:"";flex:1;height:1px;background:#888}
  .address{position:absolute;left:130px;top:128px;width:400px;text-align:center;font-size:16px;color:var(--grey);line-height:21px}

  .specialties{position:absolute;left:70px;top:186px;list-style:none;font-size:16px;line-height:21px;color:#333}
  .specialties li{display:flex;align-items:center;gap:16px}
  .specialties svg{width:12px;height:12px;flex:none}
  .specialties b{font-style:italic;font-weight:600}
  .hours{position:absolute;left:99px;top:262px;font-size:12px;font-weight:500;color:var(--grey)}

  .doctor{position:absolute;left:0;width:620px;height:178px}
  .doctor .strip{position:absolute;left:0;top:0;width:28px;height:100%;border-radius:0 6px 6px 0}
  .doctor .services{position:absolute;left:263px;top:0;width:357px;height:100%;border-radius:6px 0 0 6px;color:var(--white);font-size:12px;line-height:17px;overflow:hidden}
  .doctor .edge{position:absolute;right:0;top:0;width:28px;height:100%}
  .doctor .edge svg{position:absolute;right:0;top:50%;margin-top:-9px;width:16px;height:18px}
  .services ul{list-style:none}
  .services li{padding-left:14px;position:relative}
  .services li::before{content:"•";position:absolute;left:1px}
  .services .more{padding-left:0}
  .services .more::before{content:none}
  .services h4{font-weight:400;font-size:12px}

  .practice-mark{position:absolute;left:28px;width:235px;display:flex;justify-content:center;align-items:center;gap:8px;font-size:14px;font-weight:600}
  .practice-mark i{display:block;width:14px;height:14px;border-radius:50%}
  .doc-name{position:absolute;left:28px;width:235px;text-align:center;font-style:italic;font-weight:600;font-size:18px}
  .doc-meta{position:absolute;left:28px;width:235px;text-align:center;font-size:11px;line-height:15px;color:var(--grey)}
  .doc-meta em{font-style:italic}

  .gp{top:300px}
  .gp .strip,.gp .services{background:var(--teal)}
  .gp .edge{background:var(--teal-dark)}
  .gp .doc-name,.gp .practice-mark{color:var(--teal)}
  .gp .practice-mark i{background:var(--teal)}

  .eye{top:485px}
  .eye .strip,.eye .services{background:var(--purple)}
  .eye .edge{background:var(--purple-dark)}
  .eye .doc-name,.eye .practice-mark{color:var(--purple)}
  .eye .practice-mark i{background:var(--purple)}

  .obgyn{top:670px}
  .obgyn .strip,.obgyn .services{background:var(--navy)}
  .obgyn .edge{background:var(--navy-dark)}
  .obgyn .doc-name,.obgyn .practice-mark{color:var(--navy)}
  .obgyn .practice-mark i{background:var(--navy)}
  .obgyn .col{position:absolute;top:12px}
</style>
</head>
<body>
<main class="flyer">
  <div class="top-band"></div>

  <header>
    <div class="brand-dot"></div>
    <h1 class="brand-name">KEYSTONE MEDICAL</h1>
    <p class="tagline">Your Health is our Priority</p>
    <p class="address">42 Harbour Lane, Port Ellis, St. Marlowe<br>Tel : (555) 310 2040 / 2041</p>
  </header>

  <ul class="specialties">
    <li><svg viewBox="0 0 12 12"><path d="M1 0L12 6L1 12Z" fill="var(--teal)"/></svg><span><b>General Practitioner</b> – (555) 310 4418</span></li>
    <li><svg viewBox="0 0 12 12"><path d="M1 0L12 6L1 12Z" fill="var(--purple)"/></svg><span><b>Ophthalmologist</b> – (555) 310 7720</span></li>
    <li><svg viewBox="0 0 12 12"><path d="M1 0L12 6L1 12Z" fill="var(--navy)"/></svg><span><b>Obstetrician/Gynaecologist</b> – (555) 310 5186, (555) 310 9034</span></li>
  </ul>
  <p class="hours">Opening hours : MONDAY – FRIDAYS 9am-6pm &nbsp;•&nbsp; SATURDAYS 10am-5pm</p>

  <section class="doctor gp">
    <div class="strip"></div>
    <div class="practice-mark" style="top:58px"><i></i>Keystone Family Care</div>
    <h2 class="doc-name" style="top:118px">Dr. Marcus Whitfield</h2>
    <p class="doc-meta" style="top:142px"><em>MD. General Practitioner</em><br>marcus.whitfield.md@example.com</p>
    <div class="services">
      <ul style="position:absolute;left:17px;top:12px">
        <li>General Checks</li>
        <li>Annual Check ups</li>
        <li>Wound Care/Dressings</li>
        <li>Incision &amp; Drainage</li>
        <li>Suturing Lacerations</li>
        <li>Pain Injections</li>
        <li>Glucose Checks</li>
        <li>Foreign Body Removal</li>
        <li class="more">… and more</li>
      </ul>
      <div class="edge"><svg viewBox="0 0 16 18"><path d="M16 0L0 9L16 18Z" fill="#fff"/></svg></div>
    </div>
  </section>

  <section class="doctor eye">
    <div class="strip"></div>
    <div class="practice-mark" style="top:74px"><i></i>Clearview Eye Care</div>
    <h2 class="doc-name" style="top:118px">Dr. Lucia R. Fontaine</h2>
    <p class="doc-meta" style="top:142px"><em>MD. Surgeon Ophthalmologist</em><br>lucia.eyes@example.com</p>
    <div class="services">
      <ul style="position:absolute;left:17px;top:37px">
        <li>Eyes Disease Examination</li>
        <li>Surgery of Pterygium</li>
        <li>Cataract</li>
        <li>Glaucoma</li>
        <li>Emergency: Conjunctivitis, Traumatism, Foreign Body</li>
        <li class="more">… and more</li>
      </ul>
      <div class="edge"><svg viewBox="0 0 16 18"><path d="M16 0L0 9L16 18Z" fill="#fff"/></svg></div>
    </div>
  </section>

  <section class="doctor obgyn">
    <div class="strip"></div>
    <div class="practice-mark" style="top:50px"><i></i>Keystone Maternity</div>
    <h2 class="doc-name" style="top:108px">Dr. Arjun Mehrotra</h2>
    <p class="doc-meta" style="top:133px">BMedSci, MBBS, DM (O&amp;G), FACOG<br><em>Obstetrician &amp; Gynaecologist</em><br>drmehrotra@example.com</p>
    <div class="services">
      <div class="col" style="left:17px">
        <h4>Obstetrics :</h4>
        <ul>
          <li>Prenatal Care</li>
          <li>Delivery</li>
          <li>Postnatal Checks</li>
          <li>High Risk Pregnancy</li>
          <li class="more">… and more</li>
        </ul>
      </div>
      <div class="col" style="left:154px">
        <h4>Gynaecology :</h4>
        <ul>
          <li>Pap Smears</li>
          <li>Abnormal Vaginal Bleeding</li>
          <li>Fibroids</li>
          <li>Colposcopy</li>
          <li>Family Planning</li>
          <li>Infertility</li>
          <li>Cancer Screening</li>
          <li class="more">… and more</li>
        </ul>
      </div>
      <div class="edge"><svg viewBox="0 0 16 18"><path d="M16 0L0 9L16 18Z" fill="#fff"/></svg></div>
    </div>
  </section>
</main>
</body>
</html>
```